Book Cover Design KRT

Want a new book cover but want to use the same photo and change the sub name. This is for a brand called "Golden Rose Living". The book is called "Bare Floor, Full Power"

This is for a 8.5 * 11 book size

We really want to brand the Golden Rose Living

I've attached a sample of an old book cover, the photo I want used and the golden rose living logo
Updates

Requirements
Must have
• Must have the logo,

must have the book title. "Bare Floor, Full Power"

Must have "Featuring" The Golden Rose Living Fold Up Card Game"

On the back put the logo and Golden Rose Living Nutrition

must have the authors name "Dana Pellow" on the page

"The Sunrise Shape Guide"
Nice to have
• Golden Rose Living Presents:

the book title

```html
<!DOCTYPE html>
<html lang="en">
<head>
<meta charset="utf-8">
<title>Bare Floor, Full Power — Book Cover</title>
<link rel="stylesheet" href="https://fonts.googleapis.com/css2?family=Anton&family=Montserrat:wght@400;600;700&display=swap">
<style>
  :root {
    --page-bg: #ffffff;
    --cover-black: #0d0d0d;
    --panel-dark: #1b1b1b;
    --panel-mid: #222222;
    --brand-red: #c8050c;
    --brand-red-deep: #8f0006;
    --title-white: #ffffff;
    --sub-grey: #d9d9d9;
    --gold: #d9b24a;
    --photo-teal: #3f8f7e;
    --photo-warm: #3a2620;
    --photo-dark: #141416;
  }
  html, body {
    margin: 0;
    padding: 0;
    width: 1200px;
    height: 564px;
    overflow: hidden;
    background: var(--page-bg);
  }
  .stage {
    position: relative;
    width: 1200px;
    height: 564px;
  }
  .book-cover {
    position: absolute;
    left: 407px;
    top: 32px;
    width: 386px;
    height: 500px;
    box-shadow: 0 2px 8px rgba(0,0,0,0.25);
  }
  .cover-art { display: block; width: 100%; height: 100%; }
  .presents-line {
    font-family: "Montserrat", sans-serif;
    font-weight: 400;
    font-size: 19px;
    fill: var(--title-white);
  }
  .title-text { font-family: "Anton", sans-serif; }
  .title-red { fill: url(#redTitle); font-size: 177px; }
  .title-white { fill: url(#silverTitle); font-size: 168px; }
  .subtitle {
    font-family: "Montserrat", sans-serif;
    font-size: 34px;
  }
  .subtitle-accent { fill: var(--brand-red); font-weight: 400; }
  .subtitle-main { fill: var(--sub-grey); font-weight: 700; }
  .game-name {
    font-family: "Montserrat", sans-serif;
    font-weight: 700;
    font-size: 26px;
    fill: var(--gold);
  }
  .game-tag {
    font-family: "Montserrat", sans-serif;
    font-weight: 400;
    font-size: 17px;
    fill: var(--gold);
  }
  .author-name {
    font-family: "Montserrat", sans-serif;
    font-weight: 700;
    font-size: 29px;
    letter-spacing: 18px;
    fill: var(--title-white);
  }
</style>
</head>
<body>
<main class="stage">
  <div class="book-cover">
    <svg class="cover-art" viewBox="0 0 820 1062" xmlns="http://www.w3.org/2000/svg">
      <defs>
        <linearGradient id="redTitle" x1="0" y1="0" x2="0" y2="1">
          <stop offset="0" stop-color="#e00a12"/>
          <stop offset="1" stop-color="#9a0008"/>
        </linearGradient>
        <linearGradient id="silverTitle" x1="0" y1="0" x2="0" y2="1">
          <stop offset="0" stop-color="#ffffff"/>
          <stop offset="0.5" stop-color="#ffffff"/>
          <stop offset="0.56" stop-color="#bdbdbd"/>
          <stop offset="1" stop-color="#f0f0f0"/>
        </linearGradient>
        <linearGradient id="cornerRed" x1="0" y1="1" x2="1" y2="0">
          <stop offset="0" stop-color="var(--brand-red-deep)"/>
          <stop offset="1" stop-color="var(--brand-red)"/>
        </linearGradient>
        <radialGradient id="photoTone" cx="0.4" cy="0.45" r="0.7">
          <stop offset="0" stop-color="var(--photo-teal)"/>
          <stop offset="0.55" stop-color="var(--photo-warm)"/>
          <stop offset="1" stop-color="var(--photo-dark)"/>
        </radialGradient>
      </defs>

      <rect class="cover-base" width="820" height="1062" fill="var(--cover-black)"/>

      <g class="bg-panels">
        <polygon points="0,560 110,440 820,440 820,520 160,520 0,700" fill="var(--panel-dark)"/>
        <polygon points="520,440 820,440 820,640 680,820" fill="var(--panel-mid)"/>
        <polygon points="0,820 120,700 300,1062 170,1062" fill="var(--panel-dark)"/>
      </g>

      <rect class="author-photo" role="img" aria-label="Photo of the author posing with a teal exercise ball"
            x="300" y="420" width="400" height="642" rx="6" fill="url(#photoTone)"/>

      <polygon class="corner-accent" points="542,1062 820,657 820,1062" fill="url(#cornerRed)"/>

      <text class="presents-line" x="47" y="74" textLength="712" lengthAdjust="spacing">THE GOLDEN ROSE LIVING FITNESS PRESENTS</text>

      <text class="title-text title-red" x="50" y="242" textLength="720" lengthAdjust="spacingAndGlyphs">BARE FLOOR,</text>
      <text class="title-text title-white" x="50" y="399" textLength="720" lengthAdjust="spacingAndGlyphs">FULL POWER</text>

      <g class="subtitle">
        <text class="subtitle-accent" x="47" y="462">THE</text>
        <text class="subtitle-main" x="47" y="497">SUNRISE SHAPE</text>
        <text class="subtitle-accent" x="47" y="532">GUIDE</text>
      </g>

      <g class="featured-game">
        <text class="game-name" x="35" y="945">THE GOLDEN</text>
        <text class="game-name" x="35" y="972">ROSE</text>
        <text class="game-name" x="35" y="999">LIVING</text>
        <text class="game-tag" x="35" y="1024">FOLD UP CARD GAME</text>
      </g>

      <g class="author">
        <text class="author-name" x="800" y="992" text-anchor="end">DANA</text>
        <text class="author-name" x="800" y="1026" text-anchor="end">PELLOW</text>
      </g>
    </svg>
  </div>
</main>
</body>
</html>
```